Stationery Design Project

We need a full corporate logo and stationary design for our business zolMake. ZolMake provides 3D Printing Services to the Australian Market.

Our predominant market is the Mining and Architectural industries and our secondary market is the Entrepreneur / Start-up sector.

What we are after:

1. Logo
2. Business Card Design
3. Letterhead Design
4. Email Signature Design

File Formats we require in colour, greyscale and Black and White:

1 .AI
2 .EPS
3 .TIF
4 .PDF
5 .PNG (300 dpi)
6 .JPG (300 dpi)
7 .GIF (300 dpi)

Industry/Entity Type

Business

Requirements
Should not have
• Should Not Have:
- "Clip-Art" should not be used.

```html
<!DOCTYPE html>
<html lang="en">
<head>
<meta charset="utf-8">
<title>zolMake Stationery</title>
<link rel="stylesheet" href="https://fonts.googleapis.com/css2?family=Open+Sans:wght@300;400;600;700&display=swap">
<style>
  :root {
    --brand-blue: #2c5aa0;
    --card-blue: #2d5ba3;
    --paper: #ffffff;
    --screen: #e9e9e9;
    --backdrop: #dcdcdc;
    --ink-soft: #4a6fb0;
  }
  * { margin: 0; padding: 0; box-sizing: border-box; }
  html, body { width: 1200px; height: 1000px; overflow: hidden; }
  body {
    background: var(--backdrop);
    font-family: "Open Sans", Arial, sans-serif;
    color: var(--brand-blue);
    position: relative;
  }
  .wordmark { font-weight: 700; letter-spacing: -0.5px; line-height: 1; white-space: nowrap; }
  .tagline { font-weight: 300; line-height: 1; white-space: nowrap; }

  /* Display panel */
  .display-panel {
    position: absolute; left: 113px; top: 183px; width: 365px; height: 488px;
    background: var(--screen);
    display: flex; flex-direction: column; align-items: center; justify-content: center;
    padding-top: 60px;
  }
  .display-panel .wordmark { font-size: 44px; }
  .display-panel .tagline { font-size: 23px; margin-top: 10px; }

  /* Letterhead */
  .letterhead {
    position: absolute; left: 573px; top: 130px; width: 522px; height: 738px;
    background: var(--paper);
    box-shadow: 0 1px 3px rgba(0,0,0,0.15);
  }
  .letterhead .masthead {
    position: absolute; left: 40px; right: 48px; top: 82px;
    display: flex; align-items: center;
  }
  .letterhead .wordmark { font-size: 27px; }
  .letterhead .rule {
    flex: 1; height: 1px; margin-left: 8px; background: var(--brand-blue);
  }
  .letterhead .tagline {
    position: absolute; left: 40px; top: 115px; font-size: 15px;
  }
  .letterhead .company {
    position: absolute; right: 48px; top: 77px;
    font-size: 13px; font-weight: 600; white-space: nowrap;
  }
  .letterhead .sender {
    position: absolute; right: 48px; top: 99px; text-align: right;
  }
  .sender .line { font-size: 9px; font-weight: 700; line-height: 1; margin-bottom: 4px; white-space: nowrap; }

  /* Business cards */
  .card-front {
    position: absolute; left: 810px; top: 466px; width: 236px; height: 158px;
    background: var(--card-blue);
    color: var(--paper);
    display: flex; flex-direction: column; align-items: center; justify-content: center;
    padding-top: 40px;
    box-shadow: 0 2px 4px rgba(0,0,0,0.25);
  }
  .card-front .wordmark { font-size: 24px; }
  .card-front .tagline { font-size: 12px; margin-top: 5px; }

  .card-back {
    position: absolute; left: 823px; top: 613px; width: 238px; height: 162px;
    background: var(--paper);
    box-shadow: 0 2px 4px rgba(0,0,0,0.2);
  }
  .card-back .chevron { position: absolute; left: 5px; top: 72px; }
  .card-back .mini-brand {
    position: absolute; right: 26px; top: 30px; font-size: 9px;
  }
  .card-back .holder { position: absolute; right: 22px; top: 50px; text-align: right; }
  .holder .name { font-size: 14px; font-weight: 700; white-space: nowrap; }
  .holder .role { font-size: 9px; font-weight: 400; color: var(--ink-soft); margin-top: 1px; }
  .card-back .contact {
    position: absolute; right: 22px; top: 98px; text-align: right;
    font-size: 9px; font-weight: 400; line-height: 1.35; color: var(--ink-soft);
    white-space: nowrap;
  }
</style>
</head>
<body>

  <section class="display-panel">
    <div class="wordmark">zolMake</div>
    <div class="tagline">Ideas made solid.</div>
  </section>

  <section class="letterhead">
    <div class="masthead">
      <div class="wordmark">zolMake</div>
      <div class="rule"></div>
    </div>
    <div class="tagline">Ideas made solid.</div>
    <div class="company">zolMake Australia</div>
    <div class="sender">
      <div class="line">18 Harbour Lane, Adelaide</div>
      <div class="line">office@zolmake.com</div>
    </div>
  </section>

  <section class="card-front">
    <div class="wordmark">zolMake</div>
    <div class="tagline">Ideas made solid.</div>
  </section>

  <section class="card-back">
    <svg class="chevron" width="22" height="40" viewBox="0 0 22 40" aria-hidden="true">
      <polygon points="0,0 22,20 0,40" fill="#2d5ba3"/>
    </svg>
    <div class="mini-brand wordmark">zolMake</div>
    <div class="holder">
      <div class="name">Mara Delaney</div>
      <div class="role">3d engineer</div>
    </div>
    <div class="contact">
      <div>mara.delaney@zolmake.com</div>
      <div>tel. 02-471 30 28</div>
      <div>www.zolmake.com</div>
    </div>
  </section>

</body>
</html>
```